Pemberly's Dale Pantry Limited (Uncoded design only)

To design a new modern website to replace an existing website.
www.clothdumplings.co.uk
we want to keep the same website address and pages - unless you hae new ideas for the pages.
We are initially looking for design only (no coding requirements)
We want wording 'Pemberly's Cloth Dumplings' to be used and Pemberly's Dale Pantry Limited to be the comapny address rather than what it is now.
I attach a new logo 'Pemberly lad' and new packaing design (Zip file). NOTE the blue man is to be replaced with the new 'Pemberlys lad 'file i.e.the man with the union jack flag on his chest.
We would like coordination of the packing colourson the new website please.

Target Market(s)

Online sales to supermarkets

Industry/Entity Type

Food manufacturing

Number of Pages Required

4 page

Font styles to use
Other font styles liked:
• Happy for any choice of font styles as I'm not stuck with the font of the packaging. I'm happy to go with what you feel looks the best and we can change the package to suit

Requirements
Must have
• Links to Facepage, Snapgram and WorkLink

```html
<!DOCTYPE html>
<html lang="en">
<head>
<meta charset="utf-8">
<title>Pemberly's Cloth Dumplings – Handmade in Lancashire</title>
<link href="https://fonts.googleapis.com/css2?family=Krona+One&family=Arvo:wght@400;700&family=Poppins:wght@400;500;600&display=swap" rel="stylesheet">
<style>
:root{
  --orange:#c4652c;
  --orange-light:#e08a4f;
  --orange-dark:#9c4418;
  --beige:#e8b58f;
  --ink:#1c1c1c;
  --text:#333;
  --muted:#666;
  --dark:#2a2a2a;
  --dark-2:#3b3b3b;
  --blush:#fdf4f0;
  --white:#fff;
}
*{margin:0;padding:0;box-sizing:border-box}
html,body{width:1200px;height:3919px;overflow:hidden}
body{position:relative;font-family:'Poppins',sans-serif;color:var(--text);background:var(--white)}
.abs{position:absolute}
.btn{position:absolute;display:flex;align-items:center;justify-content:center;border-radius:22px;color:#fff;font-family:'Poppins',sans-serif;font-weight:600;font-size:14px;background:linear-gradient(90deg,var(--orange-dark),var(--orange-light));z-index:2}
.btn.black{background:#000}
.slab{font-family:'Arvo',serif;font-weight:700;color:var(--ink)}
.wide{font-family:'Krona One',sans-serif}

/* header */
.hero{position:absolute;left:0;top:0;width:1200px;height:640px;background:linear-gradient(100deg,#f4f4f4 0%,#fafafa 40%,#ececec 100%)}
.topbar{position:absolute;right:0;top:0;width:455px;height:30px;background:linear-gradient(90deg,var(--orange),var(--orange-light));border-bottom-left-radius:30px;display:flex;align-items:center;padding-left:55px;gap:14px;font-size:12px;color:#fff;z-index:3}
.topbar .social{display:flex;align-items:center;gap:5px;text-decoration:underline}
.topbar .dot{width:18px;height:18px;border:1.5px solid #fff;border-radius:50%}
.topbar .cart{margin-left:22px;text-decoration:underline;display:flex;align-items:center;gap:6px}
.logo{position:absolute;left:161px;top:10px;width:172px;height:86px;border:2px solid #333;border-radius:50% 50% 40% 40%/60% 60% 40% 40%;display:flex;align-items:center;justify-content:center;text-align:center;font-family:'Arvo',serif;font-weight:700;font-size:15px;color:#222;line-height:1.2}
.nav{position:absolute;top:54px;font-size:13px;color:#222}
.nav.active{color:var(--orange)}
.call{position:absolute;left:916px;top:46px;font-size:12px;color:#222;line-height:1.5}
.call b{color:var(--orange);font-weight:600;font-size:14px}
.hero-title{position:absolute;left:160px;top:194px;font-family:'Krona One',sans-serif;font-weight:400;font-size:41px;line-height:68px;color:var(--orange);letter-spacing:0;white-space:nowrap;z-index:2}
.hero-sub{position:absolute;left:161px;top:324px;font-size:22px;color:#111;letter-spacing:.3px;z-index:2}
.hero-plate{position:absolute;left:648px;top:112px;width:560px;height:395px;border-radius:50%;background:radial-gradient(ellipse at 55% 55%,#c58a47 0%,#e9c27a 35%,#f3f3f0 62%,#e4e4e4 80%,transparent 82%);z-index:1}

/* ways */
.ways{position:absolute;left:0;top:620px;width:1200px;height:547px;background:linear-gradient(180deg,var(--dark) 0%,var(--dark-2) 60%,#444 100%)}
.section-title{position:absolute;width:1200px;text-align:center}
.way{position:absolute;top:761px;width:203px;height:201px;border:4px solid #777;border-radius:8px;background:linear-gradient(160deg,#f1eee8,#d8b27a 55%,#2b2b2b)}
.way-label{position:absolute;top:994px;width:203px;text-align:center;font-family:'Krona One',sans-serif;font-size:14px;color:var(--beige);letter-spacing:1px}

/* about */
.about-frame{position:absolute;left:161px;top:1212px;width:367px;height:365px;border:2px solid #eee;border-radius:40px;background:#fff}
.about-img{position:absolute;left:172px;top:1221px;width:345px;height:346px;border-radius:34px;background:radial-gradient(ellipse at 50% 55%,#d8a760 0%,#efe2c4 40%,#f7f7f5 58%,#050505 60%)}
.about-thumb{position:absolute;left:415px;top:1472px;width:155px;height:151px;border:5px solid #fff;border-radius:22px;background:linear-gradient(150deg,#222,#d9c08a 50%,#5c8a3a);box-shadow:0 4px 12px rgba(0,0,0,.2)}
.about-text{position:absolute;left:627px;top:1252px;width:420px;font-size:31px;line-height:38px;letter-spacing:2.5px}

/* products */
.shop{position:absolute;left:0;top:1690px;width:1200px;height:850px;background:var(--blush)}
.rule{position:absolute;height:3px;background:linear-gradient(90deg,var(--orange-dark),var(--orange-light))}
.card{position:absolute;width:203px;background:#fff;border-radius:6px;box-shadow:0 2px 8px rgba(0,0,0,.06);overflow:hidden}
.card .photo{height:172px;position:relative}
.tag{position:absolute;left:12px;top:14px;background:#d22;color:#fff;font-size:9px;padding:2px 7px;border-radius:8px}
.card .name{position:absolute;left:14px;font-family:'Arvo',serif;font-weight:700;font-size:12.5px;color:#222;line-height:15px;letter-spacing:.5px}
.card .price{position:absolute;left:14px;font-size:16px;color:#999}
.card .cart-btn{position:absolute;width:30px;height:30px;border-radius:50%;background:var(--orange);left:124px}
.card .eye-btn{position:absolute;width:28px;height:28px;border-radius:50%;border:1.5px solid #ccc;left:162px}

/* facilities */
.fac-text{position:absolute;left:161px;top:2684px;width:420px;font-size:29px;line-height:35px;letter-spacing:1px}
.fac-photo{position:absolute;width:204px;height:205px;border:7px solid #fff;box-shadow:0 3px 12px rgba(0,0,0,.15);background:linear-gradient(160deg,#dfe5ea,#8a9aa8 50%,#2a4f8a)}

/* contact */
.contact{position:absolute;left:0;top:3150px;width:1200px;height:640px;background:linear-gradient(180deg,#121212,#1e1e1e 50%,#252525)}
.field{position:absolute;border-bottom:1px solid #555;height:24px;font-size:11.5px;color:#aaa}
.field svg{position:absolute;right:6px;top:2px}
.footer{position:absolute;left:0;top:3790px;width:1200px;height:129px;background:#000}
.f-social{position:absolute;top:3818px;width:40px;height:40px;border:2px solid var(--orange);border-radius:50%}
.copy{position:absolute;top:3880px;width:1200px;text-align:center;font-size:12px;color:#fff}
</style>
</head>
<body>

<!-- Hero -->
<section class="hero">
  <div class="abs" role="img" aria-label="Faded photo of a commercial kitchen" style="left:0;top:0;width:1200px;height:640px;background:linear-gradient(90deg,rgba(200,200,200,.35),rgba(255,255,255,0) 40%,rgba(210,210,210,.3))"></div>
</section>

<div class="topbar">
  <span class="social"><span class="dot"></span>Facepage</span>
  <span class="social"><span class="dot"></span>Snapgram</span>
  <span class="social"><span class="dot"></span>WorkLink</span>
  <span class="cart">
    <svg width="18" height="14" viewBox="0 0 18 14" fill="none" stroke="#fff" stroke-width="1.5"><path d="M1 1h3l2 8h9l2-6H5"/><circle cx="7" cy="12.5" r="1"/><circle cx="14" cy="12.5" r="1"/></svg>
    My Cart
  </span>
</div>

<div class="logo">Pemberly's<br>Dale Pantry</div>

<a class="nav active" style="left:493px">Home</a>
<a class="nav" style="left:556px">Privacy Policy</a>
<a class="nav" style="left:669px">Shop</a>
<a class="nav" style="left:726px">Delivery</a>
<a class="nav" style="left:804px">Contact</a>

<svg class="abs" style="left:876px;top:46px" width="30" height="30" viewBox="0 0 24 24" fill="none" stroke="#c4652c" stroke-width="1.5"><path d="M5 3h4l2 5-2.5 1.5a11 11 0 0 0 6 6L16 13l5 2v4a2 2 0 0 1-2 2A17 17 0 0 1 3 5a2 2 0 0 1 2-2z"/></svg>
<div class="call">Call Now:<br><b>234, Lorem Ipsum</b></div>

<div class="hero-plate" role="img" aria-label="Photo of a cloth dumpling with chips, mushy peas and a gravy jug on a white plate"></div>

<h1 class="hero-title">HANDMADE<br>IN LANCASHIRE</h1>
<p class="hero-sub">Local Apprentice Opportunity Apply Here.</p>
<a class="btn" style="left:161px;top:376px;width:151px;height:42px">Register Today</a>
<a class="btn black" style="left:321px;top:376px;width:117px;height:42px">Read More</a>

<!-- How do you like yours -->
<section class="ways">
  <div class="abs" role="img" aria-label="Faint kitchen photo behind the section" style="left:0;top:0;width:1200px;height:547px;background:radial-gradient(ellipse at 20% 70%,rgba(255,255,255,.05),transparent 60%)"></div>
</section>

<svg class="abs" style="left:0;top:430px" width="1200" height="220" viewBox="0 0 1200 220" preserveAspectRatio="none">
  <defs>
    <linearGradient id="band" x1="0" x2="1" y1="0" y2="0">
      <stop offset="0" stop-color="#c4652c"/><stop offset=".5" stop-color="#a9501e"/><stop offset="1" stop-color="#e08a4f"/>
    </linearGradient>
  </defs>
  <path d="M0 0H1200V10C900 210 320 210 0 58Z" fill="#f3f3f3"/>
  <path d="M0 58C320 210 900 210 1200 10V60C900 230 320 225 0 112Z" fill="url(#band)"/>
</svg>

<svg class="abs" style="left:589px;top:517px" width="20" height="32" viewBox="0 0 20 32" fill="none" stroke="#555" stroke-width="1.5"><path d="M10 1v28M3 22l7 8 7-8"/></svg>
<div class="abs" style="left:540px;top:556px;width:118px;text-align:center;font-size:9px;color:var(--orange);font-weight:500">SCROLL BAR</div>

<h2 class="section-title wide" style="top:676px;font-size:29px;color:var(--beige);letter-spacing:1px">HOW DO YOU LIKE YOURS</h2>

<div class="way" style="left:161px" role="img" aria-label="Photo of an oven baked dumpling with chips and peas"></div>
<div class="way" style="left:386px" role="img" aria-label="Photo of a steamed dumpling with salad and carrots"></div>
<div class="way" style="left:611px" role="img" aria-label="Photo of a microwaved dumpling with potatoes and asparagus"></div>
<div class="way" style="left:836px" role="img" aria-label="Photo of a boil-in-the-bag dumpling with peas and mash"></div>
<div class="way-label" style="left:161px">OVEN BAKE</div>
<div class="way-label" style="left:386px">STEAM</div>
<div class="way-label" style="left:611px">MICROWAVE</div>
<div class="way-label" style="left:836px">BOIL IN THE BAG</div>
<a class="btn" style="left:540px;top:1050px;width:119px;height:43px">Buy Online</a>

<!-- About -->
<div class="about-frame"></div>
<div class="about-img" role="img" aria-label="Photo of a cloth dumpling with chips, peas and gravy"></div>
<div class="about-thumb" role="img" aria-label="Photo of a dumpling with new potatoes and asparagus"></div>
<p class="about-text slab">Our cloth dumplings are made from suet pastry and the very best cuts of beefsteak without the use of any preservatives</p>
<a class="btn" style="left:628px;top:1506px;width:117px;height:44px">Read More</a>

<!-- Shop -->
<section class="shop"></section>
<h2 class="section-title slab" style="top:1752px;font-size:28px;letter-spacing:1px">LOCAL DELIVERY ONLY £1 for all ”OL” postcodes</h2>
<div class="rule" style="left:547px;top:1802px;width:106px"></div>
<p class="section-title" style="top:1830px;font-size:15px;line-height:23px;color:#555">Delivery charge Will be Applied automatically When you Proceed to checkout<br>as Local postcode Is Recognised.</p>

<!-- row 1 -->
<div class="card" style="left:161px;top:1904px;height:256px">
  <div class="photo" role="img" aria-label="Photo of a cloth dumpling pack meal with chips and peas" style="background:linear-gradient(150deg,#222,#e0c182 50%,#f2f2f2)"></div>
  <div class="name" style="top:186px">Cloth Dumplings Pack</div>
  <div class="price" style="top:228px">£12.80</div>
  <div class="cart-btn" style="top:224px"></div><div class="eye-btn" style="top:225px"></div>
</div>
<div class="card" style="left:386px;top:1904px;height:256px">
  <div class="photo" role="img" aria-label="Photo of a dumpling with custard-style sauce" style="background:linear-gradient(150deg,#111,#f1efe6 45%,#f5d98a)"><span class="tag">New Shape</span></div>
  <div class="name" style="top:186px">Cloth Dumplings Pack</div>
  <div class="price" style="top:228px">£26.80</div>
  <div class="cart-btn" style="top:224px"></div><div class="eye-btn" style="top:225px"></div>
</div>
<div class="card" style="left:611px;top:1904px;height:256px">
  <div class="photo" role="img" aria-label="Photo of meat and potato pie with salad and peas" style="background:linear-gradient(150deg,#2a2a2a,#d2a768 50%,#4f8a32)"></div>
  <div class="name" style="top:178px">Meat and Potato Pie– for<br>people</div>
  <div class="price" style="top:228px">£10.80</div>
  <div class="cart-btn" style="top:224px"></div><div class="eye-btn" style="top:225px"></div>
</div>
<div class="card" style="left:836px;top:1904px;height:256px">
  <div class="photo" role="img" aria-label="Photo of a party size meat and potato pie in a tray" style="background:linear-gradient(150deg,#3a3a3a,#d7b679 45%,#9c7a45)"></div>
  <div class="name" style="top:178px">Meat and Potato Pie<br>– Party Size</div>
  <div class="price" style="top:228px">£21.80</div>
  <div class="cart-btn" style="top:224px"></div><div class="eye-btn" style="top:225px"></div>
</div>

<!-- row 2 -->
<div class="card" style="left:161px;top:2192px;height:264px">
  <div class="photo" role="img" aria-label="Photo of beef chilli with rice and salad" style="height:173px;background:linear-gradient(150deg,#2a2a2a,#f4f1ea 45%,#7a3a1c)"></div>
  <div class="name" style="top:187px">Traditional Beef Chilli</div>
  <div class="price" style="top:234px">£32.00</div>
  <div class="cart-btn" style="top:230px"></div><div class="eye-btn" style="top:231px"></div>
</div>
<div class="card" style="left:386px;top:2192px;height:264px">
  <div class="photo" role="img" aria-label="Photo of a Christmas pudding with custard" style="height:173px;background:linear-gradient(150deg,#203020,#f0e0a0 50%,#3a1f14)"></div>
  <div class="name" style="top:187px">Christmas Pudding pack</div>
  <div class="price" style="top:234px">£15.80</div>
  <div class="cart-btn" style="top:230px"></div><div class="eye-btn" style="top:231px"></div>
</div>
<div class="card" style="left:611px;top:2192px;height:264px">
  <div class="photo" role="img" aria-label="Photo of a family size onion pie" style="height:173px;background:linear-gradient(150deg,#c9a46c,#ecd49a 50%,#8a6a3a)"></div>
  <div class="name" style="top:187px">Onion Pie – Family Size</div>
  <div class="price" style="top:234px">£06.80</div>
  <div class="cart-btn" style="top:230px"></div><div class="eye-btn" style="top:231px"></div>
</div>
<div class="card" style="left:836px;top:2192px;height:264px">
  <div class="photo" role="img" aria-label="Photo of cheese parcels with potatoes and salad" style="height:173px;background:linear-gradient(150deg,#3b6b2a,#e5c47c 50%,#f3f0e4)"><span class="tag">New Shape</span></div>
  <div class="name" style="top:187px">Cheese Parcel pack</div>
  <div class="price" style="top:234px">£9.80</div>
  <div class="cart-btn" style="top:230px"></div><div class="eye-btn" style="top:231px"></div>
</div>

<!-- Facilities -->
<p class="fac-text slab">Our purpose built facilities are dedicated to providing consistantly perfect cloth dumplings to customers worldwide</p>
<div class="rule" style="left:161px;top:2879px;width:107px"></div>
<p class="abs" style="left:161px;top:2896px;font-size:20px;color:#111">Local Apprentice Opportunity</p>
<a class="btn" style="left:161px;top:2946px;width:119px;height:44px">Apply Here</a>

<div class="fac-photo" style="left:604px;top:2636px" role="img" aria-label="Photo of staff at a pastry production line"></div>
<div class="fac-photo" style="left:835px;top:2613px;background:linear-gradient(160deg,#e8e8e8,#9aa0a6 50%,#5a5f66)" role="img" aria-label="Photo of industrial dough mixers"></div>
<div class="fac-photo" style="left:604px;top:2867px" role="img" aria-label="Photo of a worker handling trays of dumplings"></div>
<div class="fac-photo" style="left:835px;top:2844px;background:linear-gradient(160deg,#e4e6ea,#a3abb4 50%,#3a5f9a)" role="img" aria-label="Photo of a worker at stainless steel packing machines"></div>

<!-- Contact -->
<section class="contact">
  <div class="abs" role="img" aria-label="Faint photo of the production floor" style="left:0;top:0;width:1200px;height:640px;background:radial-gradient(ellipse at 50% 60%,rgba(255,255,255,.04),transparent 70%)"></div>
</section>
<svg class="abs" style="left:0;top:3120px" width="1200" height="170" viewBox="0 0 1200 170" preserveAspectRatio="none">
  <defs>
    <linearGradient id="band2" x1="0" x2="1" y1="0" y2="0">
      <stop offset="0" stop-color="#a9501e"/><stop offset=".5" stop-color="#c4652c"/><stop offset="1" stop-color="#e8955a"/>
    </linearGradient>
  </defs>
  <path d="M0 0H1200V150C900 40 500 0 0 120Z" fill="#fff"/>
  <path d="M0 120C500 0 900 40 1200 150V170H0Z" fill="url(#band2)"/>
  <path d="M0 150C500 35 900 70 1200 170V170H0Z" fill="#121212"/>
</svg>

<h2 class="section-title slab" style="top:3250px;font-size:30px;color:var(--orange-light);letter-spacing:1px">Contact Us</h2>
<p class="section-title" style="top:3331px;font-size:16px;color:#fff">Please contact us via this form and we will get back to soon..</p>

<div class="field" style="left:280px;top:3392px;width:310px">Your Name* (required)
  <svg width="12" height="14" viewBox="0 0 12 14" fill="#c4652c"><circle cx="6" cy="4" r="3"/><path d="M0 14c0-4 3-6 6-6s6 2 6 6z"/></svg></div>
<div class="field" style="left:611px;top:3392px;width:295px">Your Surname* (required)
  <svg width="12" height="14" viewBox="0 0 12 14" fill="#c4652c"><circle cx="6" cy="4" r="3"/><path d="M0 14c0-4 3-6 6-6s6 2 6 6z"/></svg></div>
<div class="field" style="left:280px;top:3453px;width:310px">Your Email*(required)
  <svg width="14" height="12" viewBox="0 0 14 12" fill="#c4652c"><path d="M0 2h14v9H0z"/><path d="M0 2l7 5 7-5" stroke="#1e1e1e" fill="none"/></svg></div>
<div class="field" style="left:611px;top:3453px;width:295px">Subject
  <svg width="14" height="14" viewBox="0 0 14 14" fill="none" stroke="#c4652c" stroke-width="1.5"><path d="M5 2h7v10H5M1 7h7M5 4l3 3-3 3"/></svg></div>
<div class="field" style="left:280px;top:3510px;width:626px;height:57px">Message
  <svg width="14" height="12" viewBox="0 0 14 12" fill="none" stroke="#c4652c" stroke-width="1.5"><path d="M1 6l6-5 6 5v5H1z"/></svg></div>
<div class="field" style="left:280px;top:3596px;width:626px;height:35px">Spam filter: What is the capital of England?
  <svg width="12" height="16" viewBox="0 0 12 16" fill="#c4652c"><path d="M6 0a6 6 0 0 1 6 6c0 4-6 10-6 10S0 10 0 6a6 6 0 0 1 6-6z"/><circle cx="6" cy="6" r="2" fill="#1e1e1e"/></svg></div>

<a class="btn" style="left:541px;top:3676px;width:118px;height:43px;font-size:13px">SUBMIT</a>

<!-- Footer -->
<footer class="footer"></footer>
<div class="f-social" style="left:512px" aria-label="Facepage"></div>
<div class="f-social" style="left:581px" aria-label="Snapgram"></div>
<div class="f-social" style="left:646px" aria-label="WorkLink"></div>
<p class="copy">© 2023 <b>Pemberly's Cloth Dumplings</b> All rights reserved.</p>

</body>
</html>
```